Business Card design for law firm = Brindlecourt Australia

We are seeking a new design for our business cards.
We are keeping our logo, which is attached.
We need space for
Name
Title
Address is , which is
Level 14
83 Tarrenby Street
Sydney NSW 2000
Phone :
Mobile :
Fax :
Email :
DX :
website www.brindlecourt.com.au

Industry/Entity Type

Law Firm / Banking and Finance

Contact Information for Business Card

We are seeking a new design for our business cards. We are keeping our logo. We need space for Name Title Address is Level 14 83 Tarrenby Street Sydney NSW 2000 Phone Mobile Fax Email DX website www.brindlecourt.com.au

Colors
0054AA
0677BA
7BADD7
CADEEF
E8F1F8

Requirements
Must have
• see our website for general feel www.brindlecourt.com.au

```html
<!DOCTYPE html>
<html lang="en">
<head>
<meta charset="utf-8">
<title>Brindlecourt Business Card</title>
<link rel="stylesheet" href="https://fonts.googleapis.com/css2?family=Mulish:wght@400;700&display=swap">
<style>
  :root {
    --backdrop: #ababab;
    --card-navy: #022d59;
    --mark-navy: #00133f;
    --card-white: #ffffff;
    --brand-blue: #1b5aa6;
    --name-blue: #0b4f9c;
    --accent-teal: #0099c0;
    --text-grey: #4a4a4a;
  }
  * { margin: 0; padding: 0; box-sizing: border-box; }
  html, body {
    width: 1200px; height: 1000px; overflow: hidden;
    background: var(--backdrop);
    font-family: "Mulish", sans-serif;
  }
  .canvas { position: relative; width: 1200px; height: 1000px; }
  .card { position: absolute; left: 341px; width: 515px; height: 298px; }
  .card-back { top: 145px; background: var(--card-navy); }
  .card-back .emblem {
    position: absolute; left: 206px; top: 98px;
    width: 102px; height: 102px; background: var(--mark-navy);
  }
  .card-front { top: 480px; background: var(--card-white); }
  .brand-square {
    position: absolute; left: 190px; top: 35px;
    width: 48px; height: 48px; background: var(--accent-teal);
  }
  .brand-name {
    position: absolute; left: 189px; top: 88px;
    font-size: 28px; font-weight: 400; color: var(--brand-blue);
    letter-spacing: -0.2px; line-height: 1;
  }
  .brand-tagline {
    position: absolute; left: 190px; top: 125px;
    font-size: 11px; color: var(--accent-teal); letter-spacing: 0.5px;
  }
  .person {
    position: absolute; right: 272px; top: 178px; text-align: right;
  }
  .person-name { font-size: 17px; font-weight: 700; color: var(--name-blue); letter-spacing: 0.3px; }
  .person-title { font-size: 13.5px; color: var(--accent-teal); margin-top: 2px; letter-spacing: 0.3px; }
  .divider {
    position: absolute; left: 257px; top: 164px;
    width: 2px; height: 68px; background: var(--accent-teal);
  }
  .contact {
    position: absolute; left: 272px; top: 171px;
    list-style: none; font-size: 12px; line-height: 14.5px; color: var(--text-grey);
  }
  .address {
    position: absolute; left: 0; right: 0; top: 267px; text-align: center;
    font-size: 13px; color: var(--text-grey); letter-spacing: 0.2px;
  }
</style>
</head>
<body>
<main class="canvas">
  <section class="card card-back">
    <div class="emblem"></div>
  </section>
  <section class="card card-front">
    <div class="brand-square"></div>
    <div class="brand-name">Brindlecourt</div>
    <div class="brand-tagline">strategic legal outsourcing</div>
    <div class="person">
      <div class="person-name">Maren Halloway</div>
      <div class="person-title">Chief Legal Officer</div>
    </div>
    <div class="divider"></div>
    <ul class="contact">
      <li>02 9184 0370</li>
      <li>02 9186 2259</li>
      <li>enquiries@brindlecourt.com.au</li>
      <li>www.brindlecourt.com.au</li>
    </ul>
    <p class="address">Level 14, 83 Tarrenby Street, Sydney NSW 2000 | DX: 418 Sydney</p>
  </section>
</main>
</body>
</html>
```